Retail Package for Ammunition Company

We are looking for a packaging design for a retail boxed ammunition. The "look". Attached will be the logo to be used. The logo is attached and a can be manipulated on the box. Box to represent strength and accuracy. Will need to provide .psd files to allow in house personnel to add/remove text to other calibers and warnings. Wow me with your designs!

Browse Other Brands: http://www.brightfalconstore.com/brands

The packaging needs to include:
Logo- provided and the following text:

FRONT 1. 9mm 115gr FMJ

BACK 2. WARNING: To avoid serious injury: (1) use only ammunition in good condition; use only in modern firearms in good condition marked for .22 Long Rifle (LR) cartridges; (2) always be sure barrel is free of any obstructions; the barrel should be checked in case of light recoil, or an unusually loud or weak sound heard during firing; (3) wear eye and ear protection; (4) if gun fails to fire, avoid exposure to breech when unloading and point muzzle in a safe direction. Keep firearm pointed in safe direction at all times; (5) discharge may occur if rim is struck; handle with caution, do not drop. (6) Do not shoot at hard surfaces or water to prevent ricochet; (7) Bullet is capable of traveling extreme distances. Know your backstop; (8) Store in cool dry place

3. LEAD WARNING: Discharging firearms in poorly ventilated areas, cleaning firearms, or handling ammunition may result in exposure to lead and other substances known to cause birth defects, reproductive harm, and other serious physical injury. Have adequate ventilation at all times. Wash hands thoroughly after exposure.

Dimensions ; (LxWxH): 5.25" x 2.625" x 1.125"

Target Market(s)

Ammunition Industry

```html
<!DOCTYPE html>
<html lang="en">
<head>
<meta charset="utf-8">
<title>Stone Ridge Armory – 9MM Box Dieline</title>
<link href="https://fonts.googleapis.com/css2?family=Roboto+Slab:wght@700&family=Archivo+Narrow:wght@700&family=Open+Sans:wght@400;700&display=swap" rel="stylesheet">
<style>
  :root {
    --brand-red: #8c1119;
    --deep-red: #6a0c12;
    --bright-red: #a3161f;
    --side-grey: #bcbdc0;
    --silver-light: #f2f2f3;
    --silver-mid: #c9cacc;
    --silver-dark: #a9aaad;
    --white: #ffffff;
    --ink: #1a1a1a;
    --warning-text: #e6d6d7;
  }
  html, body { margin: 0; padding: 0; overflow: hidden; }
  body { width: 1200px; height: 1000px; background: var(--white); position: relative; font-family: "Open Sans", Arial, sans-serif; }

  .dimensions { position: absolute; left: 613px; top: 42px; font: 400 17px Arial, sans-serif; color: var(--ink); }

  .panel { position: absolute; box-sizing: border-box; overflow: hidden; }
  .flap-top { left: 296px; top: 82px; width: 592px; height: 130px; background: var(--brand-red); }
  .flap-bottom { left: 296px; top: 525px; width: 592px; height: 130px; background: var(--brand-red); }
  .side { top: 221px; width: 131px; height: 296px; background: var(--side-grey); }
  .side-left { left: 157px; }
  .side-right { left: 895px; }
  .front { left: 296px; top: 220px; width: 592px; height: 297px; background: linear-gradient(105deg, var(--silver-dark) 0%, var(--silver-light) 35%, var(--silver-mid) 55%, var(--silver-light) 75%, var(--silver-mid) 100%); }
  .back { left: 296px; top: 661px; width: 592px; height: 297px; background: linear-gradient(160deg, var(--brand-red) 0%, var(--deep-red) 30%, var(--bright-red) 55%, var(--deep-red) 75%, var(--bright-red) 100%); }

  .lead-warning { position: absolute; left: 0; top: 0; width: 100%; height: 100%; transform: rotate(180deg); box-sizing: border-box; padding: 23px 20px 0; text-align: center; color: var(--white); font-size: 12.8px; line-height: 18px; }

  .brand-name { font-family: "Roboto Slab", Georgia, serif; font-weight: 700; color: var(--brand-red); margin: 0; }
  .brand-mark { position: absolute; left: 335px; top: 255px; width: 120px; height: 120px; border-radius: 50%; background: var(--brand-red); }
  .front-brand { position: absolute; left: 497px; top: 268px; width: 352px; text-align: center; }
  .front-brand .line-main { display: block; font-size: 47px; line-height: 58px; }
  .front-brand .line-sub { display: block; font-size: 19px; letter-spacing: 5px; line-height: 24px; }

  .side-brand { position: absolute; left: 50%; top: 50%; width: 260px; text-align: center; }
  .side-left .side-brand { transform: translate(-50%, -50%) rotate(90deg); }
  .side-right .side-brand { transform: translate(-50%, -50%) rotate(-90deg); }
  .side-brand .line-main { display: block; font-size: 25px; line-height: 30px; }
  .side-brand .line-sub { display: block; font-size: 10px; letter-spacing: 3px; line-height: 14px; }

  .front-band { position: absolute; left: 0; top: 0; }

  .caliber { position: absolute; left: 540px; top: 392px; font: 700 82px/82px "Archivo Narrow", "Arial Narrow", sans-serif; color: var(--white); }
  .load { position: absolute; left: 703px; top: 404px; width: 108px; color: var(--white); font: 700 31px/30px "Archivo Narrow", "Arial Narrow", sans-serif; text-align: center; }
  .load span { display: block; border-top: 1.5px solid var(--white); padding: 1px 0 0; }
  .load span:last-child { border-bottom: 1.5px solid var(--white); }
  .count { position: absolute; left: 617px; top: 480px; font: 700 20px Arial, sans-serif; letter-spacing: 0.5px; color: var(--white); }

  .safety-warning { position: absolute; left: 55px; top: 48px; width: 492px; margin: 0; color: var(--warning-text); font-size: 13.2px; line-height: 23.5px; }
  .safety-warning strong { font-weight: 700; }
</style>
</head>
<body>
  <div class="dimensions">(LxWxH): 5.25" x 2.625" x 1.125"</div>

  <section class="panel flap-top">
    <p class="lead-warning">LEAD WARNING: Discharging firearms in poorly ventilated areas, cleaning firearms,<br>or handling ammunition may result in exposure to lead and other substances<br>known to cause birth defects, reproductive harm, and other serious physical injury.<br>Have adequate ventilation at all times. Wash hands thorougly after exposure.</p>
  </section>

  <section class="panel side side-left">
    <p class="brand-name side-brand"><span class="line-main">STONE RIDGE</span><span class="line-sub">ARMORY</span></p>
  </section>

  <section class="panel front">
    <svg class="front-band" width="592" height="297" viewBox="0 0 592 297">
      <defs>
        <pattern id="band-lines" width="6" height="5" patternUnits="userSpaceOnUse">
          <rect width="6" height="5" fill="#8c1119"/>
          <rect y="3.5" width="6" height="1.3" fill="#5e0a10"/>
        </pattern>
      </defs>
      <polygon points="0,297 248,160 592,160 592,297" fill="#ffffff"/>
      <polygon points="14,297 255,167 592,167 592,297" fill="url(#band-lines)"/>
    </svg>
  </section>
  <div class="brand-mark"></div>
  <p class="brand-name front-brand"><span class="line-main">STONE RIDGE</span><span class="line-sub">ARMORY</span></p>
  <div class="caliber">9MM</div>
  <div class="load"><span>115GR</span><span>FMJ</span></div>
  <div class="count">50 CARTRIDGES</div>

  <section class="panel side side-right">
    <p class="brand-name side-brand"><span class="line-main">STONE RIDGE</span><span class="line-sub">ARMORY</span></p>
  </section>

  <section class="panel flap-bottom"></section>

  <section class="panel back">
    <p class="safety-warning"><strong>WARNING:</strong> To avoid serious injury: (1) use only ammunition in good condition; use only in modern firearms in good condition marked for .22 Long Rifle (LR) cartridges; (2) always be sure barrel is free of any obstructions; the barrel should be checked in case of light recoil, or an unusually loud or weak sound heard during firing; (3) wear eye and ear protection; (4) if gun fails to fire, avoid exposure to breech when unloading and point muzzle in a safe direction. Keep firearm pointed in safe direction at all times; (5) discharge may occur if rim is struck; handle with caution, do not drop. (6) Do not shoot at hard surfaces or water to prevent ricochet; (7) Bullet is capable of traveling extreme distances. Know your backstop; (8) Store in cool dry place</p>
  </section>
</body>
</html>
```